Gourmet Restaurant take out menu

We need a take out menu design that is trendy for a casual upscale Italian restaurant with a vast menu. This menu must be able to be 4 color and reproducible in large quantities to be bulked mailed or inserted into a daily paper. It must also maintain a theme that can be crossed over to our in house dining menu and specials menu.
OUR WEBSITE:
www.bellavistoplates.example
For the content, go to the Menu section of our website. We are interested in the design scheme and a template to use.
Target Market(s)
families, sinle individuals seeking take out meals and delivery
Industry/Entity Type
Restaurant
Look and feel
Each slider illustrates characteristics of the customer's brand and the style your logo design should communicate.

```html
<!DOCTYPE html>
<html lang="en">
<head>
<meta charset="utf-8">
<title>Bella Visto Italian Cuisine – Take Out Menu</title>
<link rel="stylesheet" href="https://fonts.googleapis.com/css2?family=Oswald:wght@400;500&family=Archivo+Narrow:ital,wght@0,400;0,700;1,400&family=Lato:ital,wght@0,400;1,400&display=swap">
<style>
:root{
  --orange:#f26522;
  --orange-deep:#e8561a;
  --ink:#1d1d1d;
  --paper:#ffffff;
  --cream:#f4ede4;
}
*{box-sizing:border-box;margin:0;padding:0}
html,body{width:1200px;height:928px;overflow:hidden;background:var(--paper)}
.menu{position:relative;width:1200px;height:928px;font-family:"Archivo Narrow",sans-serif;color:var(--ink)}
.abs{position:absolute}

/* section headings */
.sec-title{font-family:"Oswald",sans-serif;font-weight:400;font-size:18px;letter-spacing:.2px;line-height:1}
.served{font-family:"Oswald",sans-serif;font-size:7px;display:flex;align-items:center;gap:4px;color:var(--orange)}
.served svg{width:9px;height:9px}
.rule{height:1.5px;background:var(--orange);position:absolute}
.rule::before,.rule::after{content:"";position:absolute;top:-2px;width:5px;height:5px;border-radius:50%;background:var(--orange)}
.rule::before{left:-2px}.rule::after{right:-2px}

/* menu items */
.items{position:absolute;display:flex;flex-direction:column;justify-content:space-between;font-size:6.8px;line-height:8.3px}
.item{display:grid;grid-template-columns:1fr 34px}
.item .name{font-weight:700}
.item .price{font-weight:700;text-align:right}
.item .desc{grid-column:1/2;padding-left:8px}
.item .desc2{grid-column:2;text-align:right;font-weight:700}

/* left top band */
.top-band{left:0;top:0;width:395px;height:40px;background:var(--orange)}
.top-band .sec-title{position:absolute;left:50px;top:13px;color:var(--paper)}
.top-band .rule{left:28px;top:35px;width:165px;background:var(--paper)}
.top-band .rule::before,.top-band .rule::after{background:var(--paper)}
.top-band .served{position:absolute;left:218px;top:22px;color:var(--paper)}

/* heart healthy */
.healthy{left:412px;top:14px;width:378px;height:469px;border:1.5px solid var(--orange)}
.healthy .head{position:absolute;top:-9px;left:50px;background:var(--paper);padding:0 8px;color:var(--ink)}
.healthy .items{left:12px;top:20px;width:352px;height:438px;line-height:10.2px}
.healthy .item{grid-template-columns:1fr 30px}
.healthy .desc{padding-left:8px}

/* children + beverages */
.kids{left:396px;top:495px;width:409px;height:173px;background:var(--orange);color:var(--paper)}
.kids .sec-title{position:absolute;left:52px;top:10px;color:var(--ink)}
.kids .list{position:absolute;left:24px;top:38px;width:166px;font-size:7px;line-height:12.7px}
.row{display:flex;justify-content:space-between}
.bev{position:absolute;left:212px;top:13px;width:173px;height:150px;border:1.5px solid var(--paper)}
.bev .sec-title{position:absolute;top:-9px;left:45px;background:var(--orange);padding:0 6px}
.bev .list{left:13px;top:14px;width:150px;line-height:12.4px}
.bev .sub{display:flex;align-items:center;gap:3px;font-size:6.6px;line-height:8px;padding-left:2px}
.bev .sub span.br{font-size:20px;line-height:1;font-family:"Lato",sans-serif}

/* call to action */
.cta{left:396px;top:676px;width:409px;text-align:center}
.cta .lead{font-family:"Oswald",sans-serif;font-size:24.5px;line-height:29px;letter-spacing:-.6px;color:var(--ink);transform:scaleX(.86)}
.cta .phone{font-family:"Oswald",sans-serif;font-weight:500;font-size:27px;line-height:29px;color:var(--orange);display:flex;justify-content:center;align-items:center;gap:8px}
.cta .phone svg{width:19px;height:19px}
.cta .addr{font-family:"Lato",sans-serif;font-style:italic;font-size:21px;margin-top:8px}
.cta .web{font-family:"Lato",sans-serif;font-size:13.5px;margin-top:6px}

/* cover panel */
.cover{left:805px;top:0;width:395px;height:928px;background:radial-gradient(ellipse at 65% 68%,#b8311d 0%,#8f2616 30%,#d9b48f 60%,#f3ebe2 85%)}
.logo-box{left:829px;top:50px;width:352px;height:212px;background:var(--paper);border:1.5px solid var(--orange);outline:5px solid var(--paper)}
.logo-box .line{position:absolute;left:10px;right:10px;height:1.5px;background:var(--orange)}
.logo-name{position:absolute;left:0;right:0;top:80px;text-align:center;font-family:"Oswald",sans-serif;font-weight:400;font-size:52px;line-height:1;color:var(--orange)}
.logo-sub{position:absolute;left:0;right:0;top:142px;text-align:center;font-family:"Oswald",sans-serif;font-weight:400;font-size:15px;letter-spacing:4px;color:var(--orange)}
.cover-band{left:805px;top:268px;width:395px;height:16px;background:var(--orange);clip-path:polygon(0 0,100% 0,96% 100%,0 100%)}
.cover-title{left:963px;top:862px;font-family:"Oswald",sans-serif;font-size:29px;color:var(--paper);letter-spacing:-.5px}
</style>
</head>
<body>
<div class="menu">

  <!-- Chicken specialties -->
  <div class="abs top-band">
    <h2 class="sec-title">CHICKEN SPECIALTIES</h2>
    <div class="rule"></div>
    <div class="served"><svg viewBox="0 0 10 10"><circle cx="5" cy="5" r="5" fill="#fff"/><path d="M2.6 5.2l1.6 1.6 3.3-3.5" stroke="#f26522" stroke-width="1.3" fill="none"/></svg>SERVED WITH A HOUSE SALAD AND BREAD</div>
  </div>
  <div class="items" style="left:28px;top:44px;width:360px;height:216px">
    <div class="item"><span class="name">Chicken and Broccoli Alfredo</span><span class="price">16.99</span><span class="desc">Served over linguini pasta.</span></div>
    <div class="item"><span class="name">Chicken Dijon</span><span class="price">16.99</span><span class="desc">In a rich imported brandy dijon demi glace, served with white rice and broccoli crowns.</span></div>
    <div class="item"><span class="name">Chicken Francaise</span><span class="price">16.99</span><span class="desc">Lemon white wine butter sauce, served over linguini.</span></div>
    <div class="item"><span class="name">Chicken Panzanella</span><span class="price">16.99</span><span class="desc">Grilled chicken over field greens, Kalamata olives, red onion, cucumbers and croutons tossed in red wine vinegar.</span></div>
    <div class="item"><span class="name">Chicken Parmigiana</span><span class="price">16.59</span><span class="desc">Served with a side of linguini.</span></div>
    <div class="item"><span class="name">Chicken Rosa</span><span class="price">16.99</span><span class="desc">Chicken, sundried tomatoes, baby spinach and roasted red peppers in a Rosa cream sauce, served over penne pasta.</span></div>
    <div class="item"><span class="name">Chicken Saltimbocca</span><span class="price">16.99</span><span class="desc">Prosciutto ham and mozzarella cheese, served over fettuccine pasta with a sage-infused demi glace.</span></div>
    <div class="item"><span class="name">Parmesan Crusted Chicken</span><span class="price">15.99</span><span class="desc">Chardonnay butter sauce, served with whipped potatoes, steamed broccoli crowns.</span></div>
    <div class="item"><span class="name">Pollo DiVodka</span><span class="price">18.59</span><span class="desc">Chicken, jumbo lump crab meat, vodka-spiked Rosa sauce, on a bed of penne pasta.</span></div>
    <div class="item"><span class="name">Chicken Pesto</span><span class="price">16.99</span><span class="desc">Sautéed chicken topped with homemade pesto, sliced tomato and melted mozzarella cheese, served over penne in a pesto sauce.</span></div>
    <div class="item"><span class="name">Chicken Fontina</span><span class="price">16.99</span><span class="desc">Sautéed chicken, spinach, fontina cheese and artichokes in a lemon basil sauce, served over linguini.</span></div>
  </div>

  <!-- Fish and seafood -->
  <h2 class="abs sec-title" style="left:51px;top:266px">FISH AND SEAFOOD</h2>
  <div class="rule" style="left:33px;top:290px;width:150px"></div>
  <div class="abs served" style="left:215px;top:282px;color:var(--ink)"><svg viewBox="0 0 10 10"><circle cx="5" cy="5" r="5" fill="#f26522"/><path d="M2.6 5.2l1.6 1.6 3.3-3.5" stroke="#fff" stroke-width="1.3" fill="none"/></svg>SERVED WITH A HOUSE SALAD AND BREAD</div>
  <div class="items" style="left:28px;top:296px;width:360px;height:272px">
    <div class="item"><span class="name">Fried Shrimp Platter</span><span class="price">16.99</span><span class="desc">Complemented with French fries, coleslaw and our homemade cocktail sauce.</span></div>
    <div class="item"><span class="name">Gourmet Seafood</span><span class="price">24.99</span><span class="desc">Gulf shrimp, jumbo sea scallops, littleneck clams, sweet mussels in a spicy marinara sauce with garlic,<br>fresh herbs over linguini.</span></div>
    <div class="item"><span class="name">Horseradish Encrusted Salmon</span><span class="price">17.99</span><span class="desc">Accompanied with a whole grain mustard sauce, savory rice, seasonal vegetable.</span></div>
    <div class="item"><span class="name">Scallops Piccata</span><span class="price">20.99</span><span class="desc">Capers and spinach in a fresh lemon butter sauce, served over angel hair pasta.</span></div>
    <div class="item"><span class="name">Flounder Puttanesca</span><span class="price">17.99</span><span class="desc">Sautéed flounder filet topped with our homemade puttanesca sauce, served with rice.</span></div>
    <div class="item"><span class="name">Fried Flounder</span><span class="price">17.99</span><span class="desc">Panko breadcrumb encrusted flounder, served with coleslaw and cajun French fries.</span></div>
    <div class="item"><span class="name">Brewhouse Fish and Chips</span><span class="price">13.99</span><span class="desc">Beer battered, served with seasoned French fries and tartar sauce.</span></div>
    <div class="item"><span class="name">Shrimp Scampi</span><span class="price">18.99</span><span class="desc">Plum tomatoes, lemon butter sauce, seasoned with fresh basil and garlic over linguini.</span></div>
    <div class="item"><span class="name">Shrimp Parmigiana</span><span class="price">17.99</span><span class="desc">Topped with our homemade tomato sauce, mozzarella cheese, served with a side of linguini.</span></div>
    <div class="item"><span class="name">Tilapia Gracina</span><span class="price">18.99</span><span class="desc">Coated in a parmesan egg batter topped with lump crab meat, finished with a tomato basil butter sauce,<br>served over penne pasta.</span></div>
    <div class="item"><span class="name">Sesame Seared Tuna</span><span class="price">21.99</span><span class="desc">Black and white sesame seed encrusted ahi tuna, served with vegetables in a sweet hoisin sauce &amp; wasabi mashed.</span></div>
    <div class="item"><span class="name">Stuffed Flounder</span><span class="price">20.99</span><span class="desc">Stuffed with jumbo lump crab, drizzled with a lemon butter sauce, served with mashed potatoes &amp; mixed vegetables.</span></div>
    <div class="item"><span class="name">Salmon Chardonnay</span><span class="price">17.99</span><span class="desc">Oven braised salmon in an Unoaked Chardonnay sauce, served with mashed potatoes &amp; mixed vegetables.</span></div>
  </div>

  <!-- Pasta specialties -->
  <h2 class="abs sec-title" style="left:47px;top:581px">PASTA SPECIALTIES</h2>
  <div class="rule" style="left:30px;top:604px;width:146px"></div>
  <div class="abs served" style="left:218px;top:597px;color:var(--ink)"><svg viewBox="0 0 10 10"><circle cx="5" cy="5" r="5" fill="#f26522"/><path d="M2.6 5.2l1.6 1.6 3.3-3.5" stroke="#fff" stroke-width="1.3" fill="none"/></svg>SERVED WITH A HOUSE SALAD AND BREAD</div>
  <div class="items" style="left:31px;top:608px;width:345px;height:302px">
    <div class="item"><span class="name">Baked Lasagna</span><span class="price">12.99</span><span class="desc">Pasta sheets layered with ricotta, fresh herbs, parmesan and mozzarella cheese, tomato sauce.<br>With meat sauce.</span><span class="desc2">14.99</span></div>
    <div class="item"><span class="name">Baked Penne</span><span class="price">12.99</span><span class="desc">Ricotta cheese, fresh herbs, tomato sauce, shredded mozzarella.</span></div>
    <div class="item"><span class="name">Cheese Ravioli</span><span class="price">12.99</span><span class="desc">Ricotta cheese filled pasta, topped with tomato sauce.</span></div>
    <div class="item"><span class="name">Crab Ravioli</span><span class="price">19.59</span><span class="desc">Crabmeat and ricotta cheese ravioli, spinach, sundried tomatoes, lump crab meat in a Rosa sauce.</span></div>
    <div class="item"><span class="name">Gnocchi Pronto</span><span class="price">15.99</span><span class="desc">Roasted mushrooms, Italian sausage, baby peas and bacon, in a sundried tomato cream sauce.</span></div>
    <div class="item"><span class="name">Gnocchi Genovese</span><span class="price">13.99</span><span class="desc">Gnocchi tossed in a vodka cream sauce with melted mozzarella cheese and baked to perfection.</span></div>
    <div class="item"><span class="name">Sunday Pasta</span><span class="price">11.99</span><span class="desc">Imported pasta served with our homemade meatballs and tomato sauce.<br>Meat sauce or olive oil and garlic.</span><span class="desc2">13.99</span></div>
    <div class="item"><span class="name">Fettuccini Alfredo</span><span class="price">13.99</span><span class="desc">Fettuccini pasta tossed in a creamy alfredo sauce.</span></div>
    <div class="item"><span class="name">Linguini and Clams</span><span class="price">16.99</span><span class="desc">Baby clams, fresh herbs and olive oil, served over linguini, your choice of red or white sauce.</span></div>
    <div class="item"><span class="name">Manicotti</span><span class="price">12.99</span><span class="desc">Ricotta filled manicotti topped with tomato sauce and mozzarella cheese.</span></div>
    <div class="item"><span class="name">Penne Italiano</span><span class="price">15.99</span><span class="desc">Chicken breast, Italian sausage, broccoli robe, roasted peppers, and parmesan cheese in our homemade tomato sauce.</span></div>
    <div class="item"><span class="name">Portabella Ravioli</span><span class="price">17.99</span><span class="desc">Portabella mushroom stuffed ravioli in a sundried tomato cream sauce.</span></div>
    <div class="item"><span class="name">Tortellini Bolognese</span><span class="price">13.99</span><span class="desc">Cheese filled tortellini tossed in our meat and mushroom sauce.</span></div>
    <div class="item"><span class="name">Garden Pasta</span><span class="price">13.99</span><span class="desc">Roasted red peppers, Kalamata olives, red onion, asparagus, cherry tomatoes and spinach sautéed in olive oil<br>&amp; garlic, served over imported capellini with Pecorino Romano cheese.</span></div>
  </div>

  <!-- Heart healthy -->
  <section class="abs healthy">
    <div class="head"><h2 class="sec-title" style="font-size:17px">HEART HEALTHY</h2></div>
    <div class="abs served" style="left:160px;top:14px;color:var(--ink)"><svg viewBox="0 0 10 10"><circle cx="5" cy="5" r="5" fill="#f26522"/><path d="M2.6 5.2l1.6 1.6 3.3-3.5" stroke="#fff" stroke-width="1.3" fill="none"/></svg>SERVED WITH A HOUSE SALAD AND BREAD</div>
    <div class="items">
      <div class="item"><span class="name">Broiled Scallops</span><span class="price">13.99</span><span class="desc">Sweet lime sauce, complemented with rice, chef's vegetable.<br>Nutritional Value: Calories 265; Protein 22.7g; Carbs 32.3g; Total Fat 4g; Sat Fat 1g; Cholesterol 37mg;<br>Sodium 463mg; Potassium 404mg</span></div>
      <div class="item"><span class="name">Eggplant Pomodoro</span><span class="price">10.99</span><span class="desc">Pasta Diced eggplant, plum tomatoes, green olives and capers sautéed in olive oil and garlic, served over angel hair.<br>Nutritional Value: Calories 252; Protein 27g; Carbs 15g; Total Fat 5g; Sat Fat 1g; Cholesterol 66mg;<br>Potassium 444mg; Sodium 517mg</span></div>
      <div class="item"><span class="name">Chicken and Asparagus</span><span class="price">11.99</span><span class="desc">Plum tomatoes, asparagus, garlic and feta cheese, served over penne pasta, finished with fresh herbs, parmesan cheese.<br>Nutritional Value: Calories 282; Protein 109g; Carbs 49g; Total Fat 7g; Sat Fat 1g; Cholesterol 21mg;<br>Potassium 416mg; Sodium 467mg</span></div>
      <div class="item"><span class="name">Gnocchi Pancetta</span><span class="price">9.99</span><span class="desc">Pancetta, plum tomatoes, oil, garlic with parmesan cheese.<br>Nutritional Value: Calories 377; Protein 14g; Carbs 63g; Total Fat 7g; Sat Fat 3g; Cholesterol 16mg;<br>Potassium 329mg; Sodium 686mg</span></div>
      <div class="item"><span class="name">Flounder Olivio</span><span class="price">12.99</span><span class="desc">Extra virgin olive oil, garlic, onion, capers, green olives, julienne jalapeños, tomatoes, served with chef's vegetables.<br>Nutritional Value: Calories 276; Protein 32g; Carbs 16g; Total Fat 8g; Sat Fat 1g; Cholesterol 52mg; Sodium 566mg</span></div>
      <div class="item"><span class="name">Lemon Garlic Tilapia</span><span class="price">12.99</span><span class="desc">Tilapia sautéed with lemon, garlic, parsley, pepper and a touch of butter, served with chef's vegetable.<br>Nutritional Value: Calories 271; Protein 26g; Carbs 15g; Total Fat 9g; Sat Fat 2g; Cholesterol 58mg; Sodium 274.</span></div>
      <div class="item"><span class="name">Herb Filet</span><span class="price">15.99</span><span class="desc">Filet of beef rubbed with an herb butter and grilled, accompanied with vegetables.<br>Nutritional Value: Calories 338; Protein 31g; Carbs 18g; Total Fat 14g; Sat Fat 5g; Cholesterol 80mg;<br>Potassium 462mg; Sodium 442mg.</span></div>
      <div class="item"><span class="name">Lemon Caper Salmon</span><span class="price">12.99</span><span class="desc">Poached in a creamy lemon caper sauce, served with rice pilaf, steamed chef's choice vegetables.<br>Nutritional Value: Calories 370; Protein 26.8g; Carbs 11.3g; Total Fat 16g; Sat Fat 4g; Cholesterol 73mg;<br>Potassium 500mg; Sodium 586mg.</span></div>
      <div class="item"><span class="name">Penne Siciliano</span><span class="price">10.99</span><span class="desc">Cherry tomatoes, asparagus, goat cheese, finished with fresh basil, garlic, extra virgin olive oil.<br>Nutritional Value: Calories 381; Protein 15g; Carbs 62g; Total Fat 7g; Sat Fat 4g; Cholesterol 25mg;<br>Potassium 427mg; Sodium 329mg</span></div>
      <div class="item"><span class="name">Tuna Tempero</span><span class="price">13.99</span><span class="desc">Ahi tuna, olive relish, served with rice, broccoli crowns.<br>Nutritional Value: Calories 184; Protein 31g; Carbs 1g; Total Fat 5g; Sat Fat 1g; Cholesterol 6mg<br>Potassium 636 mg; Sodium 266mg</span></div>
      <div class="item"><span class="name">Grilled Miso Salmon</span><span class="price">12.99</span><span class="desc">Glazed with an infused soy sauce and sweet rice wine reduction, finished with fresh cilantro, sesame seeds,<br>served with steamed Asian vegetables.<br>Nutritional Value: Calories 282; Protein 29g; Carbs 4g; Total Fat 10g; Sat Fat 2g; Cholesterol 78mg; Sodium 382mg</span></div>
    </div>
  </section>

  <!-- Children's menu and beverages -->
  <section class="abs kids">
    <h2 class="sec-title">CHILDREN'S MENU</h2>
    <div class="rule" style="left:30px;top:33px;width:160px;background:var(--paper)"></div>
    <div class="list">
      <div class="row"><span>Cheeseburger and Fries</span><span>5.99</span></div>
      <div class="row"><span>Chicken Fingers and Fries</span><span>6.59</span></div>
      <div class="row"><span>Grilled Cheese and Fries</span><span>5.99</span></div>
      <div class="row"><span>Grilled Chicken Breast with Buttered Pasta</span><span>6.99</span></div>
      <div class="row"><span>Linguini and Meatball</span><span>6.99</span></div>
      <div class="row"><span>Mac and Cheese</span><span>4.99</span></div>
      <div class="row"><span>Mini Pizza</span><span>5.99</span></div>
      <div class="row"><span>Ravioli and Meatball</span><span>6.99</span></div>
      <div class="row"><span>Sliders (2) and Fries</span><span>5.99</span></div>
    </div>
    <div class="bev">
      <h2 class="sec-title">BEVERAGES</h2>
      <div class="list abs" style="font-size:7px">
        <div class="row"><span>16 oz Bottled Tea</span><span>1.99</span></div>
        <div class="row"><span>Home-Brewed Iced Tea</span><span>1.99</span></div>
        <div class="row"><span>20 oz Bottles</span><span>1.99</span></div>
        <div class="sub"><span class="br">{</span><span>Cola, Diet Cola, Orange, Ginger Ale,<br>Lemon-Lime, Root Beer</span><span class="br">}</span></div>
        <div class="row"><span>2 Liter Bottles</span><span>2.99</span></div>
        <div class="sub"><span class="br">{</span><span>Cola, Diet Cola, Orange, Ginger Ale,<br>Lemon-Lime, Root Beer</span><span class="br">}</span></div>
        <div class="row"><span>16 oz Bottled Water</span><span>1.59</span></div>
      </div>
    </div>
  </section>

  <!-- Catering call to action -->
  <section class="abs cta">
    <p class="lead">HAVE A MEETING, &nbsp;BIG PARTY OR &nbsp;NEED<br>A FOOD CATERING, &nbsp;JUST CALL US AT</p>
    <p class="phone"><svg viewBox="0 0 24 24"><path d="M6.6 2.5c.6-.4 1.4-.3 1.8.3l2.3 3.4c.4.6.3 1.3-.2 1.8L9 9.4c1.2 2.5 3.1 4.4 5.6 5.6l1.4-1.5c.5-.5 1.2-.6 1.8-.2l3.4 2.3c.6.4.7 1.2.3 1.8l-1.3 2c-.6.9-1.7 1.3-2.8 1C9.6 18.4 5.6 14.4 3.6 6.6c-.3-1.1.1-2.2 1-2.8z" fill="#f26522"/></svg>555 310 4820</p>
    <p class="phone"><svg viewBox="0 0 24 24"><rect x="6" y="2" width="12" height="6" fill="#f26522"/><rect x="2" y="9" width="20" height="9" rx="1.5" fill="#f26522"/><rect x="6" y="15" width="12" height="7" fill="#f26522" stroke="#fff" stroke-width="1.2"/></svg>555 310 4821</p>
    <p class="lead">AND WE WILL HAPPY TO<br>SERVE EVERYTHING FOR YOU.</p>
    <p class="addr">18 Harbor Lane Millbrook, CA</p>
    <p class="web">or log on to our website &nbsp;www.bellavistoplates.example</p>
  </section>

  <!-- Cover panel -->
  <div class="abs cover" role="img" aria-label="Photograph of a plate of spaghetti with meatballs in tomato sauce, a fork twirling pasta and a basil leaf"></div>
  <div class="abs cover-band"></div>
  <div class="abs logo-box">
    <div class="line" style="top:10px"></div>
    <div class="logo-name">Bella Visto</div>
    <div class="logo-sub">ITALIAN CUISINE</div>
    <div class="line" style="bottom:10px"></div>
  </div>
  <div class="abs cover-title">THE MENU</div>

</div>
</body>
</html>
```